Web Design Front Page Only for Organic Skincare

We have been in business for nearly 20 years. We are run by all females and sell anything from aromatherapy, skincare and pharmacy types products to health food shops and pharmacy. We are looking for an attractive and colourful but simple front web page design for our wholesale customers to look at. We want our customers to start using our website to find information rather than ringing us. So we want it to be attractive to our buyers who are young and funky.
Updates

To give you an idea of the products we sell to pharmacy and health food shops also beauty shops and hair salons.  We mainly deal with organic body and skincare, aromatherapy oils and body products, but also do some simple pharmacy products such as bandages and pill boxes, finger splits, walking frames and wheelchairs.  We are only looking for the front page of the website.  The back-end will be done in-house.  We currently do not have a logo designed so I am thinking that once we have done the website design we can build a logo from it.  I like bright colours and want something that is inviting to further discover that we do many different types of products.

Target Market(s)

young girls who are our retail buyers

Industry/Entity Type

Pharmacy

Requirements
Must have
• A section which says

Customer Log in
Should not have
• don't worry about too much writing or tabs. We will insert these later. Just come up with design image.

```html
<!DOCTYPE html>
<html lang="en">
<head>
<meta charset="utf-8">
<title>Verdane Wellness</title>
<link href="https://fonts.googleapis.com/css2?family=Questrial&family=Arimo:wght@400;700&family=Archivo+Narrow:wght@400;500&display=swap" rel="stylesheet">
<style>
:root{
  --olive:#b3b96d;
  --olive-dark:#9ea55a;
  --copper:#cd9457;
  --maroon:#7c2a35;
  --maroon-text:#8a2a3a;
  --cream:#f6ecd0;
  --cream-light:#fbf6e6;
  --pale:#fbfcd0;
  --sand:#ddd5c8;
  --lead:#9a7848;
  --body:#333;
  --white:#fff;
}
*{box-sizing:border-box;margin:0;padding:0}
html,body{width:1170px;height:1200px;overflow:hidden}
body{background:linear-gradient(90deg,var(--pale),#fdfde8 50%,var(--pale));font-family:"Arimo",Arial,sans-serif;position:relative}
.header{position:absolute;left:0;top:0;width:1170px;height:139px;background:var(--olive)}
.brand{position:absolute;left:140px;top:46px;display:flex;align-items:center;gap:12px;font-family:"Questrial",sans-serif;font-size:28px;color:var(--white)}
.brand-dot{width:48px;height:48px;border-radius:50%;background:#8fc85a}
.login{position:absolute;left:828px;top:57px}
.login input{display:block;width:175px;height:24px;border:none;border-radius:12px;background:var(--white);padding:0 14px;font:italic 10px "Arimo",sans-serif;color:var(--lead);margin-bottom:9px}
.login input::placeholder{color:var(--lead)}
.login-btn{position:absolute;left:184px;top:33px;width:40px;height:24px;border:none;border-radius:3px;background:#fbf7c8;font:bold 10px "Arimo",sans-serif;color:#6b5a2a}
.login-links{position:absolute;left:14px;top:66px;width:180px;display:flex;gap:30px;font-size:10px}
.login-links a{color:var(--white)}
.page{position:absolute;left:119px;top:139px;width:933px}
.nav{height:47px;background:var(--copper);display:flex}
.nav a{font-family:"Questrial",sans-serif;font-size:17px;color:var(--white);text-decoration:none;display:flex;align-items:center;justify-content:center;border-right:1px solid #dcab77}
.nav a:last-child{border-right:none}
.hero{position:relative;height:243px;overflow:hidden}
.hero-photo{position:absolute;inset:0;background:linear-gradient(90deg,#6aa63a 0%,#a9d46a 22%,#e7f2d4 42%,#f4e3d8 60%,#efd9cc 80%,#f7f2ee 100%)}
.hero-band{position:absolute;left:0;top:0}
.promo{height:89px;background:var(--olive);position:relative}
.promo p{position:absolute;left:23px;top:29px;width:620px;font-family:"Questrial",sans-serif;font-weight:700;font-size:14.5px;line-height:19px;color:var(--white)}
.promo-btn{position:absolute;left:688px;top:14px;width:212px;height:62px;border-radius:31px;background:linear-gradient(#fbf7c8,#f4ecb0);font-family:"Questrial",sans-serif;font-size:14.5px;line-height:19px;color:#8a7440;padding:12px 0 0 28px}
.promo-btn svg{position:absolute;right:16px;top:22px}
.content{display:flex;height:446px;background:var(--white)}
.side{width:243px;background:linear-gradient(var(--cream) 70%,var(--white))}
.side a{display:flex;align-items:center;height:45px;border-bottom:1px solid #efe2bd;padding-left:23px;gap:12px;font-family:"Questrial",sans-serif;font-size:13px;color:#8a7440;text-decoration:none}
.side a::before{content:"";border-left:8px solid #6e6a5c;border-top:5px solid transparent;border-bottom:5px solid transparent}
.main{flex:1;padding:31px 60px 0 30px}
.main h1{font-family:"Questrial",sans-serif;font-weight:700;font-size:19px;color:var(--maroon-text);margin-bottom:18px}
.lead{font-weight:700;font-size:11.5px;line-height:17px;color:var(--lead);margin-bottom:18px}
.main p.body{font-size:9.7px;line-height:17px;color:var(--body);margin-bottom:17px}
.specials{position:absolute;left:21px;top:825px;width:894px;height:168px;background:var(--sand)}
.specials h2{position:absolute;left:56px;top:1px;font-family:"Questrial",sans-serif;font-weight:700;font-size:14px;color:var(--maroon-text)}
.arrow{position:absolute;top:66px}
.card{position:absolute;top:19px;height:138px;background:var(--white);padding:22px 0 0 15px}
.card h3{font-family:"Archivo Narrow",sans-serif;font-weight:500;font-size:13px;line-height:14px;color:var(--maroon-text);width:200px}
.card p{font-size:8.5px;line-height:10.5px;color:#222;width:100px;margin-top:9px}
.card a{display:block;font-size:9px;color:var(--maroon-text);text-decoration:none;margin-top:12px}
.product{position:absolute;right:12px;bottom:12px;width:110px;height:80px;border-radius:6px}
.footer{position:absolute;left:0;top:993px;width:933px;height:36px;background:var(--olive);text-align:center;line-height:36px;font-size:10px;color:var(--white)}
</style>
</head>
<body>
<header class="header">
  <div class="brand"><span>Verdane</span><span class="brand-dot"></span></div>
  <form class="login">
    <input type="text" placeholder="Username">
    <input type="password" placeholder="Password">
    <button class="login-btn" type="button">Login</button>
    <div class="login-links"><a href="#">Register</a><a href="#">Forgotten password</a></div>
  </form>
</header>

<div class="page">
  <nav class="nav">
    <a href="#" style="width:287px">AROMATHERAPY OILS</a>
    <a href="#" style="width:193px">SKINCARE</a>
    <a href="#" style="width:240px">BODY PRODUCTS</a>
    <a href="#" style="width:213px">PHARMACY</a>
  </nav>

  <section class="hero">
    <div class="hero-photo" role="img" aria-label="Aloe vera leaf close-up beside two women with fresh, clear skin"></div>
    <svg class="hero-band" width="360" height="243" viewBox="0 0 360 243">
      <polygon points="0,80 0,192 325,0 203,0" fill="#7c2a35"/>
      <g fill="#fff" font-family="Arimo, sans-serif" font-weight="700" font-size="14">
        <text transform="translate(36,104) rotate(-30.5)">Lorem ipsum dolor sit</text>
        <text transform="translate(12,143) rotate(-30.5)">amet, consectetur adipisicing elit</text>
      </g>
    </svg>
  </section>

  <section class="promo">
    <p>Sed ut perspiciatis unde omnis iste natus error sit voluptatem accusantium doloremque laudantium, totam rem aperiam, eaque ipsa quae ab illo</p>
    <div class="promo-btn">At vero eos et<br>accusamus et iusto
      <svg width="18" height="20"><polygon points="0,0 18,10 0,20" fill="#6e6a5c"/></svg>
    </div>
  </section>

  <section class="content">
    <aside class="side">
      <a href="#">Sed ut perspiciatis</a>
      <a href="#">unde omnis iste natus</a>
      <a href="#">error sit voluptatem</a>
      <a href="#">tium doloremque laud</a>
      <a href="#">totam rem aperiam</a>
      <a href="#">quae ab illo inventore ve</a>
      <a href="#">et quasi architecto bea</a>
    </aside>
    <main class="main">
      <h1>Welcome to Verdane Wellness</h1>
      <p class="lead">Lorem ipsum dolor sit amet, consectetur adipisicing elit, sed do eiusmod tempor incididunt ut labore et dolore magna aliqua. Ut enim ad minim veniam, quis nostrud exercitation ullamco laboris nisi ut aliquip ex ea commodo consequat.</p>
      <p class="body">Sed ut perspiciatis unde omnis iste natus error sit voluptatem accusantium doloremque laudantium, totam rem aperiam, eaque ipsa quae ab illo inventore veritatis et quasi architecto beatae vitae dicta sunt explicabo. Nemo enim ipsam voluptatem quia voluptas sit aspernatur aut odit aut fugit, sed quia consequuntur magni dolores eos qui ratione voluptatem sequi nesciunt. Neque porro quisquam est, qui dolorem ipsum quia dolor sit amet, consectetur, adipisci velit, sed quia non numquam eius modi tempora incidunt ut labore et dolore magnam aliquam quaerat voluptatem. Ut enim ad minima veniam, quis nostrum exercitationem ullam corporis suscipit laboriosam, nisi ut aliquid ex ea commodi consequatur? Quis autem vel eum iure reprehenderit qui in ea voluptate velit esse quam nihil molestiae consequatur, vel illum qui dolorem eum fugiat quo voluptas nulla pariatur</p>
      <p class="body">At vero eos et accusamus et iusto odio dignissimos ducimus qui blanditiis praesentium voluptatum deleniti atque corrupti quos dolores et quas molestias excepturi sint occaecati cupiditate non provident, similique sunt in culpa qui officia deserunt mollitia animi, id est laborum et dolorum fuga. Et harum quidem rerum facilis est et expedita distinctio. Nam libero tempore, cum soluta nobis est eligendi optio cumque nihil impedit quo minus id quod maxime placeat facere possimus, omnis voluptas assumenda est, omnis dolor repellendus. Temporibus autem quibusdam et aut officiis debitis aut rerum nec.</p>
    </main>
  </section>

  <section class="specials">
    <h2>SPECIALS</h2>
    <svg class="arrow" style="left:16px" width="18" height="38"><polygon points="18,0 0,19 18,38" fill="#b8ab98"/></svg>
    <svg class="arrow" style="right:14px" width="18" height="38"><polygon points="0,0 18,19 0,38" fill="#b8ab98"/></svg>

    <article class="card" style="left:44px;width:258px">
      <h3>AT VERO eos et accusamus et iusto odio dignissimos ducimus</h3>
      <p>At vero eos et accus amus et iusto odio dignissimos ducimus qui blanditiis praese</p>
      <a href="#">&gt;View</a>
      <div class="product" role="img" aria-label="Aloe vera cream box and green jar" style="background:linear-gradient(135deg,#f1e0b0,#d8e9a4 60%,#a8cf5a)"></div>
    </article>
    <article class="card" style="left:327px;width:252px">
      <h3>AT VERO eos et accusamus et iusto odio dignissimos ducimus</h3>
      <p>At vero eos et accus amus et iusto odio dignissimos ducimus qui blanditiis praese</p>
      <a href="#">&gt;View</a>
      <div class="product" role="img" aria-label="Silver jar of day cream" style="background:linear-gradient(#f2f0ea,#c9c5bb 70%,#a9a396)"></div>
    </article>
    <article class="card" style="left:603px;width:244px">
      <h3>AT VERO eos et accusamus et iusto odio dignissimos ducimus</h3>
      <p>At vero eos et accus amus et iusto odio dignissimos ducimus qui blanditiis praese</p>
      <a href="#">&gt;View</a>
      <div class="product" role="img" aria-label="Foundation tube and box" style="background:linear-gradient(90deg,#f1e4d6,#e9c49a 60%,#d99e62)"></div>
    </article>
  </section>

  <footer class="footer">Verdane Wellness Pty Ltd © 2012</footer>
</div>
</body>
</html>
```